Business Card Design Project

This design is a slimline business card 45mm x90mm, the card will be printed at 49mm x 94mm and cut to 45mm x90 mm, this needs to be considered in the design. The content required on the front and back of the business card is attached in a pdf; the design will be done using photo shop as we use CS6 in our business. The design needs to be developed using a CMYK colour pallet, the main colours used on our business are red, grey black and white. A snapshot of our business brochure and new website has been provided to give you an understanding on our businesses look and feel.
FRONT OF BUSINESS CARD
Director
Marcus Feld
Ph+61 0421780213
www.brightvanecontracting.com.au
marcusfeld@brightvanecontracting.com.au
BACK OF BUSINESS CARD
SUPPORTING CLIENTS IN
Oil & Gas I Minerals & Metals I Petrochemical I Manufacturing
Building & Construction I Telecommunication I Rail I Civil I New Industries
KNOWLEDGE I EXPERTISE I EXPERIENCE I CAPACITY

```html
<!DOCTYPE html>
<html lang="en">
<head>
<meta charset="utf-8">
<title>Brightvane Contracting – Business Card</title>
<link rel="stylesheet" href="https://fonts.googleapis.com/css2?family=Arimo:wght@400;700&display=swap">
<style>
  :root {
    --red: #e31b23;
    --red-dark: #9c0c12;
    --black: #000000;
    --ink: #231f20;
    --paper: #ffffff;
    --grey-light: #f4f4f5;
    --grey-mid: #cfd0d2;
    --border: #6d6e71;
  }
  html, body {
    margin: 0;
    padding: 0;
    width: 1000px;
    height: 1200px;
    overflow: hidden;
    background: var(--paper);
    font-family: "Arimo", Arial, sans-serif;
  }
  .canvas { position: relative; width: 1000px; height: 1200px; }
  .card {
    position: absolute;
    left: 28px;
    width: 943px;
    height: 491px;
    outline: 1px solid var(--border);
    overflow: hidden;
  }
  .card--front { top: 82px; }
  .card--back { top: 625px; }
  .card__art { position: absolute; inset: 0; width: 943px; height: 491px; display: block; }

  .contact {
    position: absolute;
    right: 27px;
    top: 68px;
    text-align: right;
    color: var(--ink);
  }
  .contact__name { font-weight: 700; font-size: 27px; line-height: 32px; margin: 0; }
  .contact__role { font-size: 22px; line-height: 29px; margin: 0; }
  .contact__phone { font-size: 22px; line-height: 30px; margin: 0; }
  .contact__web, .contact__email { font-size: 18.5px; line-height: 26px; margin: 0; }

  .brand {
    position: absolute;
    left: 178px;
    top: 318px;
    display: flex;
    align-items: center;
    gap: 22px;
  }
  .brand__dot {
    width: 70px; height: 70px; border-radius: 50%;
    background: var(--red);
    flex: none;
  }
  .brand__text { display: flex; flex-direction: column; }
  .brand__name {
    font-weight: 700;
    font-size: 46px;
    line-height: 52px;
    color: var(--black);
    letter-spacing: 0.5px;
    margin: 0;
  }
  .brand__tagline { font-size: 16.5px; line-height: 22px; color: var(--ink); margin: 4px 0 0 2px; }

  .sectors {
    position: absolute;
    left: 0;
    width: 806px;
    top: 240px;
    text-align: center;
    color: var(--ink);
    font-size: 20px;
    line-height: 25.5px;
  }
  .sectors__heading { color: var(--red); margin: 0; }
  .sectors__list { margin: 0; }
  .values {
    position: absolute;
    left: 0;
    width: 806px;
    top: 440px;
    text-align: center;
    color: var(--red);
    font-size: 20px;
    margin: 0;
  }
</style>
</head>
<body>
<main class="canvas">

  <section class="card card--front" aria-label="Front of business card">
    <svg class="card__art" viewBox="0 0 943 491" aria-hidden="true">
      <defs>
        <linearGradient id="front-swoosh" x1="0" y1="1" x2="1" y2="0">
          <stop offset="0" stop-color="var(--red)"/>
          <stop offset="0.55" stop-color="var(--red)"/>
          <stop offset="1" stop-color="var(--red-dark)"/>
        </linearGradient>
        <linearGradient id="front-paper" x1="0" y1="0" x2="0" y2="1">
          <stop offset="0" stop-color="var(--grey-light)"/>
          <stop offset="0.35" stop-color="var(--grey-mid)"/>
          <stop offset="1" stop-color="var(--paper)"/>
        </linearGradient>
      </defs>
      <rect width="943" height="491" fill="var(--black)"/>
      <path d="M430,0 C180,80 0,230 0,360 C0,440 90,480 195,491 L943,491 L943,0 Z" fill="url(#front-swoosh)"/>
      <path d="M855,0 C500,60 100,220 75,370 C65,440 130,480 210,491 L943,491 L943,0 Z" fill="url(#front-paper)"/>
    </svg>

    <div class="contact">
      <p class="contact__name">Marcus Feld</p>
      <p class="contact__role">Director</p>
      <p class="contact__phone">Ph+61 0497365128</p>
      <p class="contact__web">www.brightvanecontracting.com.au</p>
      <p class="contact__email">marcusfeld@brightvanecontracting.com.au</p>
    </div>

    <div class="brand">
      <span class="brand__dot" aria-hidden="true"></span>
      <div class="brand__text">
        <p class="brand__name">BRIGHTVANE CONTRACTING</p>
        <p class="brand__tagline">Providing Effective Project Controls and Management Solutions</p>
      </div>
    </div>
  </section>

  <section class="card card--back" aria-label="Back of business card">
    <svg class="card__art" viewBox="0 0 943 491" aria-hidden="true">
      <defs>
        <linearGradient id="back-swoosh" x1="0" y1="0" x2="1" y2="1">
          <stop offset="0" stop-color="var(--red-dark)"/>
          <stop offset="0.5" stop-color="var(--red)"/>
          <stop offset="1" stop-color="var(--red)"/>
        </linearGradient>
        <linearGradient id="back-paper" x1="0" y1="0" x2="0" y2="1">
          <stop offset="0" stop-color="var(--grey-light)"/>
          <stop offset="0.3" stop-color="var(--grey-mid)"/>
          <stop offset="1" stop-color="var(--paper)"/>
        </linearGradient>
      </defs>
      <rect width="943" height="491" fill="var(--black)"/>
      <path d="M15,0 L515,0 C780,70 943,200 943,330 L943,491 L745,491 Z" fill="url(#back-swoosh)"/>
      <path d="M0,0 L15,0 C400,60 740,180 820,320 C850,380 835,450 745,491 L0,491 Z" fill="url(#back-paper)"/>
    </svg>

    <div class="sectors">
      <p class="sectors__heading">SUPPORTING CLIENTS IN</p>
      <p class="sectors__list">Oil &amp; Gas I Minerals &amp; Metals I Petrochemical I<br>
        Manufacturing Building &amp; Construction I Telecommunication I<br>
        Rail ICivil I New Industries</p>
    </div>
    <p class="values">KNOWLEDGE I EXPERTISE I EXPERIENCE I CAPACITY</p>
  </section>

</main>
</body>
</html>
```